Skin Care business card for esthetician that is home based

I need a business card for my esthetician business. I would like to use a picture provided.
I want the picture #1 that I have provided to be as the main background with my title and the moto underneath in smaller lettering. Below that as a seperate thing I would like my full name and underneath in small letters to say "esthetician".
As a seperate paragraph I would like my address then phone number, email and my website that I have provided in the business card details.
On the back side I would like my second picture to be small and in the top left corner and then have the "nice to haves" details to be at the center bottom of the card.
Target Market(s)
mosty women between 18 and 60 years old
Industry/Entity Type
Skin Care
Contact Information for Business Card
Coastline Skin Care - Main Title
Helping you find beautiful! - motto
Lorena Bistrica Vondel -
Phone: 312.485.1937
7183 SW 9th Avenue
Dallow WA 98321
marlowskincare@examplemail.com
www.marlowskincare.example
Font styles to use
Requirements
Must have
- Picure I provided or other similar photo.
Nice to have
- On the back side:
Helping you find beautiful!
www.marlowskincare.example

```html
<!DOCTYPE html>
<html lang="en">
<head>
<meta charset="UTF-8">
<title>Coastline Skin Care – Business Card</title>
<link rel="stylesheet" href="https://fonts.googleapis.com/css2?family=Libre+Baskerville&family=Montserrat:wght@300;400;600&display=swap">
<style>
  :root {
    --page-bg: #d9d8d8;
    --card-white: #ffffff;
    --ink: #1c1c1c;
    --ink-soft: #333333;
    --cream: #f1e7dc;
    --cream-deep: #e6d6c4;
    --band-brown: #5b2f1f;
    --band-light: #f4ebe2;
    --towel-brown: #7a4a36;
    --photo-skin: #d8a98e;
  }
  * { margin: 0; padding: 0; box-sizing: border-box; }
  html, body {
    width: 1200px; height: 800px; overflow: hidden;
    background: var(--page-bg);
  }
  .canvas { position: relative; width: 1200px; height: 800px; }
  .card {
    position: absolute; left: 300px; width: 600px; height: 333px;
    overflow: hidden;
    box-shadow: 0 6px 18px rgba(0,0,0,0.18);
  }

  /* Back side */
  .card--back { top: 47px; background: var(--card-white); }
  .portrait {
    position: absolute; left: 0; top: 20px; width: 250px; height: 313px;
    background: linear-gradient(180deg, #d9c39a 0%, #e9dfd4 40%, #f4f4f4 75%, #ffffff 100%);
  }
  .back-copy {
    position: absolute; left: 290px; top: 200px; width: 290px; text-align: center;
    color: var(--ink); white-space: nowrap;
  }
  .back-motto {
    font-family: "Montserrat", sans-serif; font-weight: 300;
    font-size: 16px; letter-spacing: 0.5px;
  }
  .back-web {
    margin-top: 14px;
    font-family: "Montserrat", sans-serif; font-weight: 600; font-size: 17px;
  }

  /* Front side */
  .card--front { top: 420px; }
  .hero-photo {
    position: absolute; inset: 0;
    background:
      linear-gradient(180deg, transparent 94%, var(--towel-brown) 94%),
      linear-gradient(90deg, var(--photo-skin) 0%, var(--cream-deep) 35%, var(--cream) 60%, var(--band-light) 100%);
  }
  .owner {
    position: absolute; right: 26px; top: 40px; text-align: right; color: var(--ink);
    white-space: nowrap;
  }
  .owner-name { font-family: "Libre Baskerville", serif; font-size: 14px; }
  .owner-title {
    margin-top: 6px;
    font-family: "Montserrat", sans-serif; font-size: 6px; letter-spacing: 1.5px;
  }
  .title-band {
    position: absolute; left: 370px; right: 0; top: 130px; height: 74px;
    background: var(--band-brown); color: var(--band-light);
    padding: 16px 24px 0 12px; text-align: right; white-space: nowrap;
  }
  .business-name { font-family: "Libre Baskerville", serif; font-size: 17px; font-weight: 400; }
  .business-motto {
    margin-top: 14px;
    font-family: "Montserrat", sans-serif; font-size: 8px; letter-spacing: 1.5px;
  }
  .contact {
    position: absolute; right: 18px; top: 224px; list-style: none;
    font-family: "Montserrat", sans-serif; font-size: 7.5px; color: var(--ink-soft);
    white-space: nowrap;
  }
  .contact li {
    display: flex; justify-content: flex-end; align-items: center; gap: 8px;
    height: 11px;
  }
  .contact .gap { height: 3px; }
  .contact svg { width: 9px; height: 9px; fill: var(--ink-soft); }
  .icon-space { width: 9px; display: inline-block; }
</style>
</head>
<body>
<div class="canvas">

  <section class="card card--back" aria-label="Card back">
    <div class="portrait" role="img" aria-label="Photo of the esthetician in a white uniform, smiling"></div>
    <div class="back-copy">
      <p class="back-motto">HELPING YOU FIND BEAUTIFUL!</p>
      <p class="back-web">www.marlowskincare.example</p>
    </div>
  </section>

  <section class="card card--front" aria-label="Card front">
    <div class="hero-photo" role="img" aria-label="Photo of a woman relaxing with a facial mask while receiving a face massage, with spa candle and stones"></div>

    <div class="owner">
      <p class="owner-name">Lorena Bistrica Vondel</p>
      <p class="owner-title">ESTHETICIAN</p>
    </div>

    <div class="title-band">
      <h1 class="business-name">Coastline Skin Care</h1>
      <p class="business-motto">HELPING YOU FIND BEAUTIFUL!</p>
    </div>

    <ul class="contact">
      <li>312.485.1937
        <svg viewBox="0 0 24 24"><path d="M6.6 10.8a15.2 15.2 0 0 0 6.6 6.6l2.2-2.2a1 1 0 0 1 1-.25 11.4 11.4 0 0 0 3.6.57 1 1 0 0 1 1 1V20a1 1 0 0 1-1 1A17 17 0 0 1 3 4a1 1 0 0 1 1-1h3.5a1 1 0 0 1 1 1c0 1.25.2 2.45.57 3.57a1 1 0 0 1-.25 1z"/></svg>
      </li>
      <li class="gap"></li>
      <li>7183 SW 9th Avenue
        <svg viewBox="0 0 24 24"><path d="M12 2a7 7 0 0 0-7 7c0 5.25 7 13 7 13s7-7.750 7-13a7 7 0 0 0-7-7zm0 9.5A2.5 2.5 0 1 1 12 6.5a2.5 2.5 0 0 1 0 5z"/></svg>
      </li>
      <li>Dallow WA 98321 <span class="icon-space"></span></li>
      <li class="gap"></li>
      <li>marlowskincare@examplemail.com
        <svg viewBox="0 0 24 24"><path d="M2 5h20v14H2zm2 2v.5l8 5 8-5V7z"/></svg>
      </li>
      <li class="gap"></li>
      <li>www.marlowskincare.example
        <svg viewBox="0 0 24 24"><path d="M12 2a10 10 0 1 0 0 20 10 10 0 0 0 0-20zm6.9 9h-3a15 15 0 0 0-1.3-5.6A8 8 0 0 1 18.9 11zM12 4c.9 1.2 1.8 3.5 2 7h-4c.2-3.5 1.1-5.8 2-7zM9.4 5.4A15 15 0 0 0 8.1 11h-3a8 8 0 0 1 4.3-5.6zM5.1 13h3a15 15 0 0 0 1.3 5.6A8 8 0 0 1 5.1 13zM12 20c-.9-1.2-1.8-3.5-2-7h4c-.2 3.5-1.1 5.8-2 7zm2.6-1.4a15 15 0 0 0 1.3-5.6h3a8 8 0 0 1-4.3 5.6z"/></svg>
      </li>
    </ul>
  </section>

</div>
</body>
</html>
```